Consulting/Brand Licensing business needs business card

We need a business card created for our IP company, that also does consulting and brand licensing. We would like this card to be vague, as our other business' are in the cannabis industry and this is a non-cannabis touching entity. Perhaps something that hints vaguely at the industry without alerting or possibly offending the receiver.

Target Market(s)

CEOs/Key Decision Makers/Industry Leaders

Contact Information for Business Card

No address, simply list Seattle, WA. Phone: 206-555-0147. Name: Dilan Vesterby // email: Dilan@pulvanixa.com

Colors

Designer to choose colors to be used in the design.

Requirements
Must have
• Logo, Name, Email, Phone number, "Consulting, Licensing and Branding Specialists"
Nice to have
• We would like this to be more professional than playful.

```html
<!DOCTYPE html>
<html lang="en">
<head>
<meta charset="utf-8">
<title>Pulvanixa Business Card</title>
<link href="https://fonts.googleapis.com/css2?family=Didact+Gothic&display=swap" rel="stylesheet">
<style>
  :root {
    --page: #ffffff;
    --ink: #1a1a1a;
    --rust: #d04a30;
    --rust-deep: #822510;
    --ring: #6e1c1e;
    --white: #ffffff;
    --edge: #555555;
  }
  html, body {
    margin: 0;
    padding: 0;
    width: 1200px;
    height: 1000px;
    overflow: hidden;
    background: var(--page);
    font-family: "Didact Gothic", "Century Gothic", sans-serif;
  }
  .sheet {
    position: relative;
    width: 1200px;
    height: 1000px;
  }
  .side-label {
    position: absolute;
    left: 0;
    width: 1200px;
    text-align: center;
    font-size: 22px;
    letter-spacing: 1px;
    color: var(--ink);
  }
  .side-label--front { top: 93px; }
  .side-label--back { top: 504px; }
  .card {
    position: absolute;
    left: 323px;
    width: 545px;
    height: 311px;
    overflow: hidden;
    box-shadow: 0 0 0 1px var(--edge);
  }
  .card--front { top: 132px; }
  .card--back { top: 546px; }
  .card__art {
    position: absolute;
    inset: 0;
    display: block;
  }
  .holder-name {
    position: absolute;
    margin: 0;
    color: var(--white);
    font-size: 22px;
    font-weight: 400;
    letter-spacing: 1.5px;
    white-space: nowrap;
  }
  .card--front .holder-name { left: 56px; top: 142px; }
  .card--back .holder-name { left: 288px; top: 55px; }

  .brand {
    position: absolute;
    display: flex;
    flex-direction: column;
    align-items: center;
    transform: translateX(-50%);
  }
  .card--front .brand { left: 417px; top: 118px; }
  .card--back .brand { left: 135px; top: 118px; }
  .brand__lockup {
    display: flex;
    align-items: center;
    gap: 9px;
  }
  .brand__mark {
    width: 26px;
    height: 26px;
    background: var(--rust);
    flex: none;
  }
  .brand__name {
    margin: 0;
    color: var(--rust);
    font-size: 28px;
    font-weight: 400;
    line-height: 1;
    white-space: nowrap;
  }
  .brand__tagline {
    margin: 14px 0 0;
    color: var(--ink);
    font-size: 13px;
    line-height: 1.35;
    text-align: center;
    letter-spacing: 0.3px;
  }

  .contact-list {
    position: absolute;
    left: 288px;
    top: 122px;
    margin: 0;
    padding: 0;
    list-style: none;
  }
  .contact-item {
    display: flex;
    align-items: center;
    height: 20px;
    margin-bottom: 31px;
    color: var(--white);
    font-size: 15px;
    letter-spacing: 0.5px;
  }
  .contact-icon {
    width: 20px;
    height: 20px;
    margin-right: 11px;
    flex: none;
  }
</style>
</head>
<body>
<main class="sheet">
  <div class="side-label side-label--front">Front</div>

  <section class="card card--front">
    <svg class="card__art" viewBox="0 0 545 311" width="545" height="311" aria-hidden="true">
      <defs>
        <radialGradient id="frontGlow" cx="217" cy="160" r="300" gradientUnits="userSpaceOnUse">
          <stop offset="0" stop-color="#d04a30"/>
          <stop offset="1" stop-color="#822510"/>
        </radialGradient>
        <linearGradient id="frontSwoosh" x1="0" y1="1" x2="1" y2="0">
          <stop offset="0" stop-color="#4a0c06"/>
          <stop offset="1" stop-color="#9e2a24"/>
        </linearGradient>
      </defs>
      <rect width="545" height="311" fill="url(#frontGlow)"/>
      <path d="M145 311 Q235 262 282 162 L298 178 Q286 262 318 311 Z" fill="url(#frontSwoosh)"/>
      <circle cx="492" cy="196" r="216" fill="var(--ring)"/>
      <circle cx="484" cy="198" r="202" fill="var(--white)"/>
    </svg>
    <h1 class="holder-name">Dilan Vesterby</h1>
    <div class="brand">
      <div class="brand__lockup">
        <span class="brand__mark"></span>
        <p class="brand__name">Pulvanixa, Inc</p>
      </div>
      <p class="brand__tagline">Consulting, Licensing<br>and Branding Specialists</p>
    </div>
  </section>

  <div class="side-label side-label--back">Back</div>

  <section class="card card--back">
    <svg class="card__art" viewBox="0 0 545 311" width="545" height="311" aria-hidden="true">
      <defs>
        <radialGradient id="backGlow" cx="317" cy="174" r="300" gradientUnits="userSpaceOnUse">
          <stop offset="0" stop-color="#d04a30"/>
          <stop offset="1" stop-color="#822510"/>
        </radialGradient>
      </defs>
      <rect width="545" height="311" fill="url(#backGlow)"/>
      <circle cx="62" cy="197" r="219" fill="var(--ring)"/>
      <circle cx="57" cy="199" r="205" fill="var(--white)"/>
    </svg>
    <div class="brand">
      <div class="brand__lockup">
        <span class="brand__mark"></span>
        <p class="brand__name">Pulvanixa, Inc</p>
      </div>
      <p class="brand__tagline">Consulting, Licensing<br>and Branding Specialists</p>
    </div>
    <h2 class="holder-name">Dilan Vesterby</h2>
    <ul class="contact-list">
      <li class="contact-item">
        <svg class="contact-icon" viewBox="0 0 20 20" aria-hidden="true">
          <path d="M10 1.5a5.5 5.5 0 0 0-5.5 5.5c0 4.2 5.5 11 5.5 11s5.5-6.8 5.5-11A5.5 5.5 0 0 0 10 1.5z" fill="var(--white)"/>
          <circle cx="10" cy="7" r="2" fill="var(--rust)"/>
        </svg>
        Seattle
      </li>
      <li class="contact-item">
        <svg class="contact-icon" viewBox="0 0 20 20" aria-hidden="true">
          <path d="M5 2.5l3 3.5-1.8 2.2c1 2.2 2.8 4 5 5l2.2-1.8 3.5 3-1.8 2.8C9.5 17 3 10.5 2.2 4.3z" fill="var(--white)"/>
        </svg>
        206-555-0147
      </li>
      <li class="contact-item">
        <svg class="contact-icon" viewBox="0 0 20 20" aria-hidden="true">
          <rect x="0.5" y="4" width="19" height="13" fill="var(--white)"/>
          <path d="M0.5 4.5l9.5 7 9.5-7M0.5 16.5l7-6M19.5 16.5l-7-6" fill="none" stroke="var(--rust)" stroke-width="1"/>
        </svg>
        Dilan@pulvanixa.com
      </li>
    </ul>
  </section>
</main>
</body>
</html>
```